Business Card Design Project

New Business Card design for Varodine Technology Ltd using new Logo and new Tagline for staffing company.

About us from our website - www.varodine.example:

VaroDine is a leading and recognized Electronic Entertainment, Workforce Augmentation, and Project Management solutions provider with clients in Electronic Entertainment, Legal, Technology, Government and other verticals that range in size from start up organizations to Zenlar 500 companies. VaroDine is certified as an 8(a) minority and woman owned enterprise, established in 1998.

Target Market(s)

Companies in Electronic Entertainment, Legal, Government and Technology

Industry/Entity Type

Business

Requirements
Must have
• Must include in small letters the following information on back:

Established in 1998
8(a)(w)(e), Cage #7KRT9, DUNS #462137580

Front should have the following:
Derek Holloway
Vice President
5820 Birchmont Road
Fallowby, FB 482917
555-318-2746 X 100
555-902-6613 Fax
555-318-2746 Toll Free
name@varodine.example

Our Tagline: Connect • Collaborate • Achieve

```html
<!DOCTYPE html>
<html lang="en">
<head>
<meta charset="utf-8">
<title>Varodine Technology Ltd — Business Card</title>
<link rel="stylesheet" href="https://fonts.googleapis.com/css2?family=Arimo:wght@400;700&display=swap">
<style>
  :root {
    --stage-top: #e4e4e4;
    --stage-bottom: #c9c9c9;
    --card-black: #000000;
    --card-edge: #6e6e6e;
    --brand-blue: #1b5e9b;
    --text-white: #ffffff;
    --text-muted: #a9a9a9;
    --rule-grey: #8a8a8a;
  }
  * { box-sizing: border-box; margin: 0; padding: 0; }
  html, body {
    width: 1200px;
    height: 533px;
    overflow: hidden;
  }
  body {
    background: linear-gradient(to bottom, var(--stage-top), var(--stage-bottom));
    font-family: "Arimo", Arial, Helvetica, sans-serif;
    position: relative;
  }
  .card {
    position: absolute;
    width: 510px;
    height: 294px;
    background: var(--card-black);
    border: 1px solid var(--card-edge);
    overflow: hidden;
  }
  .card--front { left: 53px; top: 112px; }
  .card--back  { left: 640px; top: 114px; height: 292px; }
  .card__band {
    position: absolute;
    left: 0; right: 0; bottom: 0;
    height: 15px;
    background: var(--brand-blue);
  }

  /* Front */
  .identity {
    position: absolute;
    left: 41px;
    top: 44px;
    color: var(--text-white);
  }
  .identity__name {
    font-size: 26px;
    font-weight: 700;
    line-height: 1;
    margin-bottom: 5px;
  }
  .identity__line {
    font-size: 15px;
    line-height: 17.5px;
  }
  .divider {
    position: absolute;
    left: 302px;
    top: 41px;
    width: 1px;
    height: 124px;
    background: var(--rule-grey);
  }
  .contact {
    position: absolute;
    left: 314px;
    top: 44px;
    color: var(--text-white);
    font-size: 15px;
    line-height: 17.8px;
    list-style: none;
  }

  /* Wordmark */
  .wordmark {
    position: absolute;
    display: flex;
    align-items: center;
    gap: 8px;
    color: var(--text-white);
    font-weight: 700;
    font-size: 27px;
    letter-spacing: -0.5px;
  }
  .wordmark__dot {
    width: 14px;
    height: 14px;
    border-radius: 50%;
    background: var(--brand-blue);
    flex: none;
  }
  .card--front .wordmark { left: 52px; top: 164px; }
  .card--back .wordmark {
    left: 50%;
    top: 116px;
    transform: translateX(-50%);
  }

  /* Back */
  .tagline {
    position: absolute;
    left: 0; right: 0;
    top: 160px;
    text-align: center;
    color: var(--text-white);
    font-size: 12px;
    letter-spacing: 1px;
  }
  .credentials {
    position: absolute;
    left: 0; right: 0;
    top: 248px;
    text-align: center;
    color: var(--text-muted);
    font-size: 13.5px;
  }
</style>
</head>
<body>

  <section class="card card--front" aria-label="Business card front">
    <div class="identity">
      <h1 class="identity__name">Derek Holloway</h1>
      <p class="identity__line">Vice President</p>
      <p class="identity__line">Varodine Technology Ltd</p>
    </div>

    <div class="divider"></div>

    <ul class="contact">
      <li>5820 Birchmont Road</li>
      <li>Fallowby, FB 482917</li>
      <li>555-318-2746 X 100</li>
      <li>555-902-6613 Fax</li>
      <li>555-318-2746 Toll Free</li>
      <li>name@varodine.example</li>
    </ul>

    <div class="wordmark">
      <span class="wordmark__dot"></span>
      <span class="wordmark__name">VaroDine</span>
    </div>

    <div class="card__band"></div>
  </section>

  <section class="card card--back" aria-label="Business card back">
    <div class="wordmark">
      <span class="wordmark__dot"></span>
      <span class="wordmark__name">VaroDine</span>
    </div>

    <p class="tagline">Connect • Collaborate • Achieve</p>

    <p class="credentials">Established in 1998 8(a)(w)(e), Cage #7KRT9, DUNS #462137580</p>

    <div class="card__band"></div>
  </section>

</body>
</html>
```